E-Book-Cover-Design im Stil eines magischen Buches gesucht
Zielgruppe
Zielgruppe: Paganerds (heidnische Klugscheißer), Geisterbegeisterte, Leute, die Bücher von Hembrick oder Lindqvorn lesen, die sich für Magie, Mythologie, Hexerei interessieren.
Aufgabenstellung
Es sollte wie ein magisches Buch aussehen.
Es wäre schön, auf die in der Einladung erwähnte schwarze Kammer anzuspielen, dort hängt über dem Altar das Luft-Tattwa, ein Kreis in luftig-hellem Blau auf schwarzem Grund.
Ansonsten eine Art Rahmen, vielleicht sowas wie magische Siegel, die das gefährliche Buch unter Kontrolle halten.
Es wäre toll, wenn die Schrift, der Name 'Mira Tolvane' und der Titel 'Vom Nebelreich' im Zusammenhang mit dem hellen Kreis ein passendes kalligraphisches Bild ergeben könnten.
Die angefügten Bilder dienen als Orientierungshilfe.
Falls es nach dem ebook eine Printversion gibt, wäre es schön, auf dem ebook-cover-Design aufzubauen.

```html
<!DOCTYPE html>
<html lang="de">
<head>
<meta charset="utf-8">
<title>Vom Nebelreich – Mira Tolvane</title>
<link rel="stylesheet" href="https://fonts.googleapis.com/css2?family=Pirata+One&display=swap">
<style>
  :root {
    --stage: #c8cbd1;
    --cover: #1e1e1f;
    --silver: #e4e4e4;
    --ornament: #3b3b3d;
    --tattwa-blue: #1a3ae0;
    --ring: #0d0d0e;
  }
  * { margin: 0; padding: 0; box-sizing: border-box; }
  html, body {
    width: 1200px;
    height: 960px;
    overflow: hidden;
    background: var(--stage);
  }
  .canvas {
    position: relative;
    width: 1200px;
    height: 960px;
    display: flex;
    align-items: center;
    justify-content: center;
  }
  .book-cover {
    position: relative;
    width: 600px;
    height: 860px;
    background: var(--cover);
    box-shadow: 0 12px 30px rgba(0,0,0,0.25);
  }
  .cover-art {
    position: absolute;
    inset: 0;
    width: 100%;
    height: 100%;
  }
  .frame-line, .guide-arc {
    fill: none;
    stroke: var(--silver);
    stroke-width: 2.5;
  }
  .ornament-area { fill: var(--ornament); }
  .tattwa-ring { fill: var(--ring); stroke: var(--silver); stroke-width: 3; }
  .tattwa-air { fill: var(--tattwa-blue); }
  .book-title {
    position: absolute;
    top: 168px;
    left: 0;
    width: 100%;
    text-align: center;
    font-family: "Pirata One", serif;
    font-size: 78px;
    line-height: 0.9;
    color: var(--silver);
    letter-spacing: 1px;
  }
  .book-author {
    position: absolute;
    top: 660px;
    left: 0;
    width: 100%;
    text-align: center;
    font-family: "Pirata One", serif;
    font-size: 44px;
    color: var(--silver);
    letter-spacing: 1px;
  }
</style>
</head>
<body>
<main class="canvas">
  <article class="book-cover">
    <svg class="cover-art" viewBox="0 0 600 860" xmlns="http://www.w3.org/2000/svg">
      <!-- side brackets, double lines -->
      <g class="frame">
        <path class="frame-line" d="M90 40 H32 V820 H90"/>
        <path class="frame-line" d="M82 52 H44 V808 H82"/>
        <path class="frame-line" d="M510 40 H568 V820 H510"/>
        <path class="frame-line" d="M518 52 H556 V808 H518"/>
      </g>
      <!-- large guiding arcs -->
      <path class="guide-arc" d="M150 92 A200 200 0 0 0 250 420"/>
      <path class="guide-arc" d="M450 92 A200 200 0 0 1 350 420"/>
      <path class="guide-arc" d="M250 440 A200 200 0 0 0 150 768"/>
      <path class="guide-arc" d="M350 440 A200 200 0 0 1 450 768"/>
      <!-- flourish areas -->
      <rect class="ornament-area" x="150" y="60" width="300" height="60" rx="30" role="img" aria-label="Geschwungene Zierranke oben"/>
      <rect class="ornament-area" x="98" y="370" width="110" height="120" rx="40" role="img" aria-label="Geschwungene Zierranke links des Kreises"/>
      <rect class="ornament-area" x="392" y="370" width="110" height="120" rx="40" role="img" aria-label="Geschwungene Zierranke rechts des Kreises"/>
      <rect class="ornament-area" x="150" y="740" width="300" height="60" rx="30" role="img" aria-label="Geschwungene Zierranke unten"/>
      <!-- air tattwa -->
      <circle class="tattwa-ring" cx="300" cy="430" r="104"/>
      <circle class="tattwa-air" cx="300" cy="430" r="90"/>
    </svg>
    <h1 class="book-title">Vom<br>Nebelreich</h1>
    <p class="book-author">Mira Tolvane</p>
  </article>
</main>
</body>
</html>
```